Commercial Business Card - stand out, clean, simple, unique.

commercial real estate group located in Texas. Called 4 Ridges Real Estate. We want a unique yet clean and professional card. On one side I would like the 4R to be by itself or to look as unique or tasteful as possible. We have the logo in white, black, and color in case a black background or something similar looks best on one side. We need a space for our name, email, cell. website. And possibly room for a phrase or city.

Contact Information for Business Card

Name, Title, Email, Phone Number, website

```html
<!DOCTYPE html>
<html lang="en">
<head>
<meta charset="utf-8">
<title>4 Ridges Real Estate – Business Card</title>
<link rel="stylesheet" href="https://fonts.googleapis.com/css2?family=Cinzel:wght@400&family=Roboto:wght@400&display=swap">
<style>
  :root {
    --backdrop: #b9b9b9;
    --card: #f4f4f4;
    --navy: #1f2d5c;
    --navy-deep: #141828;
    --royal: #28438c;
    --orange: #d3692a;
    --red: #c23a2b;
    --ink: #1d1d1f;
    --shadow: rgba(0,0,0,0.28);
  }
  * { margin: 0; padding: 0; box-sizing: border-box; }
  html, body { width: 1200px; height: 576px; overflow: hidden; }
  body { background: var(--backdrop); position: relative; font-family: "Roboto", Arial, sans-serif; }

  .card {
    position: absolute;
    top: 139px;
    width: 484px;
    height: 293px;
    background: var(--card);
    border-radius: 11px;
    overflow: hidden;
    box-shadow: 2px 4px 8px var(--shadow);
  }
  .card--front { left: 82px; }
  .card--back { left: 602px; }

  /* Front */
  .front-lockup {
    position: absolute;
    left: 0; right: 0;
    top: 98px;
    display: flex;
    justify-content: center;
    align-items: center;
    gap: 16px;
  }
  .front-lockup__square { width: 46px; height: 46px; background: var(--navy); }
  .front-lockup__divider { width: 1px; height: 60px; background: var(--navy); }
  .front-brand {
    font-family: "Cinzel", Georgia, serif;
    font-weight: 400;
    color: var(--navy);
    text-align: center;
  }
  .front-brand__name { font-size: 34px; line-height: 1; letter-spacing: 1px; }
  .front-brand__sub { font-size: 14px; letter-spacing: 7px; margin-top: 6px; margin-right: -7px; }
  .front-web {
    position: absolute;
    left: 0; right: 0;
    top: 250px;
    display: flex;
    align-items: center;
    justify-content: center;
    gap: 12px;
    font-size: 12.5px;
    color: var(--ink);
  }
  .front-web__rule { width: 48px; height: 2px; background: var(--orange); border-radius: 1px; }
  .front-band {
    position: absolute;
    left: 0; right: 0; bottom: 0;
    height: 8px;
    display: flex;
  }
  .front-band__cool { flex: 1; background: linear-gradient(90deg, var(--royal), var(--navy-deep)); }
  .front-band__warm { flex: 1; background: linear-gradient(90deg, var(--red), var(--orange)); }

  /* Back */
  .back-panel { position: absolute; left: 0; top: 0; }
  .back-info {
    position: absolute;
    right: 20px;
    top: 26px;
    text-align: right;
    color: var(--ink);
  }
  .back-brand { font-family: "Cinzel", Georgia, serif; font-weight: 400; color: var(--navy); }
  .back-brand__name { font-size: 31px; line-height: 1; letter-spacing: 0.5px; }
  .back-brand__sub { font-size: 13px; letter-spacing: 6px; margin-top: 4px; margin-right: -6px; }
  .back-person { margin-top: 27px; }
  .back-person__name { font-family: "Cinzel", Georgia, serif; font-size: 20px; color: var(--navy); line-height: 1; }
  .back-person__title { font-size: 12px; margin-top: 6px; }
  .back-contacts { margin-top: 45px; list-style: none; font-size: 13px; }
  .back-contacts li { display: flex; justify-content: flex-end; align-items: center; gap: 8px; height: 18.5px; }
  .back-contacts svg { width: 11px; height: 11px; fill: var(--orange); }
  .back-address { font-size: 13px; margin-top: 5px; }
</style>
</head>
<body>

  <section class="card card--front" aria-label="Business card front">
    <div class="front-lockup">
      <span class="front-lockup__square" aria-hidden="true"></span>
      <span class="front-lockup__divider" aria-hidden="true"></span>
      <div class="front-brand">
        <div class="front-brand__name">4 RIDGES</div>
        <div class="front-brand__sub">REAL ESTATE</div>
      </div>
    </div>
    <div class="front-web">
      <span class="front-web__rule"></span>
      <span>www.4ridgesrealestate.com</span>
      <span class="front-web__rule"></span>
    </div>
    <div class="front-band"><span class="front-band__cool"></span><span class="front-band__warm"></span></div>
  </section>

  <section class="card card--back" aria-label="Business card back">
    <svg class="back-panel" width="484" height="293" viewBox="0 0 484 293" aria-hidden="true">
      <defs>
        <linearGradient id="panelFill" x1="0" y1="0" x2="0" y2="1">
          <stop offset="0" stop-color="#28438c"/>
          <stop offset="0.55" stop-color="#1e2a5e"/>
          <stop offset="1" stop-color="#141828"/>
        </linearGradient>
      </defs>
      <path d="M0 0 H196 Q256 146 196 293 H0 Z" fill="#d3692a"/>
      <path d="M0 0 H190 Q248 146 190 293 H0 Z" fill="url(#panelFill)"/>
    </svg>

    <div class="back-info">
      <div class="back-brand">
        <div class="back-brand__name">4 RIDGES</div>
        <div class="back-brand__sub">REAL ESTATE</div>
      </div>
      <div class="back-person">
        <div class="back-person__name">Daniel Reyes</div>
        <div class="back-person__title">Managing Director</div>
      </div>
      <ul class="back-contacts">
        <li>512-555-0148
          <svg viewBox="0 0 24 24" aria-label="phone"><path d="M6.6 10.8a15 15 0 0 0 6.6 6.6l2.2-2.2c.3-.3.7-.4 1-.2 1.1.4 2.3.6 3.6.6.6 0 1 .4 1 1V20c0 .6-.4 1-1 1A17 17 0 0 1 3 4c0-.6.4-1 1-1h3.5c.6 0 1 .4 1 1 0 1.3.2 2.5.6 3.6.1.3 0 .7-.2 1z"/></svg>
        </li>
        <li>www.4ridgesrealestate.com
          <svg viewBox="0 0 24 24" aria-label="web"><circle cx="12" cy="12" r="10" fill="none" stroke="#d3692a" stroke-width="2"/><path d="M2 12h20M12 2c3 3 3 17 0 20M12 2c-3 3-3 17 0 20" fill="none" stroke="#d3692a" stroke-width="1.6"/></svg>
        </li>
        <li>dreyes@4ridgesrealestate.com
          <svg viewBox="0 0 24 24" aria-label="email"><path d="M2 5h20v14H2z"/><path d="M2 5l10 8 10-8" fill="none" stroke="#f4f4f4" stroke-width="1.8"/></svg>
        </li>
      </ul>
      <div class="back-address">118 Cedar Lane, Austin, TX 73301</div>
    </div>
  </section>

</body>
</html>
```